We are needing a bookcover for a reprint of our book "Whispers Beneath the Amber Horizon". It takes a look at the geologic formation found in the great plains. Our original cover was colorful and showed rock layers. Something similar but different and eye catching would be great. a geologic cross section showing various layers or possibly some different rocks/soils. We are really open to suggestions attached is the current book cover with the colored layers and the cover from the 80s.

Target Market(s)

Adult Readers

Industry/Entity Type

Nonprofit retail - science - nature

Requirements
Must have
• Geology or rock layers
Nice to have
• Books title, Geologic cross section
Should not have
• People or animals, no photos prefer sketch

```html
<!DOCTYPE html>
<html lang="en">
<head>
<meta charset="utf-8">
<title>Whispers Beneath the Amber Horizon — Cover Spread</title>
<link href="https://fonts.googleapis.com/css2?family=Cinzel:wght@400;500&family=PT+Sans:wght@400&display=swap" rel="stylesheet">
<style>
  :root {
    --sky-deep: #3f8fb8;
    --sky-light: #9cc6dc;
    --cloud: #e9eef0;
    --mountain: #6f94b3;
    --haze: #a9c2c9;
    --meadow: #7fbf3a;
    --meadow-dark: #5a9a2a;
    --soil-rust: #8a5432;
    --soil-brown: #6b4a35;
    --strata-dark: #243338;
    --ink: #111417;
    --paper: #ffffff;
    --spine-shade: rgba(40, 50, 60, 0.25);
  }
  * { margin: 0; padding: 0; box-sizing: border-box; }
  html, body { width: 1200px; height: 898px; overflow: hidden; background: #ffffff; }
  .cover-spread {
    position: relative;
    width: 1200px;
    height: 898px;
    overflow: hidden;
  }
  .landscape-art {
    position: absolute;
    inset: 0;
    background: linear-gradient(to bottom,
      var(--sky-light) 0%,
      var(--sky-deep) 10%,
      var(--cloud) 24%,
      var(--sky-light) 32%,
      var(--cloud) 37%,
      var(--mountain) 42%,
      var(--haze) 47%,
      var(--haze) 51%,
      var(--meadow) 54%,
      var(--meadow-dark) 58%,
      var(--soil-brown) 60%,
      var(--soil-rust) 64%,
      var(--strata-dark) 68%,
      var(--soil-rust) 73%,
      var(--strata-dark) 79%,
      var(--strata-dark) 87%,
      var(--meadow) 91%,
      var(--meadow-dark) 100%);
  }
  .spine-fold {
    position: absolute;
    top: 0;
    left: 592px;
    width: 8px;
    height: 898px;
    background: var(--spine-shade);
  }
  .back-title {
    position: absolute;
    left: 64px;
    top: 192px;
    width: 490px;
    font-family: "Cinzel", serif;
    font-weight: 400;
    font-size: 37px;
    line-height: 47px;
    letter-spacing: 1.5px;
    color: var(--ink);
    text-align: center;
  }
  .back-blurb {
    position: absolute;
    left: 60px;
    top: 590px;
    width: 488px;
    font-family: "PT Sans", sans-serif;
    font-size: 12.5px;
    line-height: 27px;
    color: var(--paper);
    text-align: center;
  }
  .category-label {
    position: absolute;
    left: 62px;
    top: 835px;
    font-family: "Cinzel", serif;
    font-size: 13px;
    letter-spacing: 0.5px;
    color: var(--paper);
  }
  .front-title {
    position: absolute;
    left: 640px;
    top: 540px;
    width: 520px;
    font-family: "Cinzel", serif;
    color: var(--paper);
    text-align: center;
    text-shadow: 0 2px 6px rgba(0, 0, 0, 0.45);
  }
  .front-title span { display: block; }
  .front-title .line-small { font-size: 36px; line-height: 42px; }
  .front-title .line-huge { font-size: 86px; line-height: 82px; letter-spacing: 1px; }
  .front-title .line-mid { font-size: 42px; line-height: 56px; }
  .front-title .line-large { font-size: 58px; line-height: 70px; }
</style>
</head>
<body>
  <main class="cover-spread">
    <div class="landscape-art" role="img" aria-label="Landscape illustration: blue sky with white clouds over distant snow-capped mountains, a green prairie, and an exposed cross section of brown and dark rock strata beneath the grass, mirrored across back and front covers"></div>
    <div class="spine-fold"></div>

    <section class="back-cover">
      <h2 class="back-title">WHISPERS BENEATH<br>THE AMBER HORIZON</h2>
      <p class="back-blurb">
        We are needing a bookcover for a reprint of our book "Whispers Beneath the<br>
        Amber Horizon". It takes a look at the geologic formation found in the great plains.<br>
        Our original cover was colorful and showed rock layers.<br>
        Something similar but different and eye catching would be great.<br>
        A geologic cross section showing various layers or possibly some different rocks/-<br>
        soils. We are really open to suggestions attached is the current book cover with<br>
        the colored layers and the cover from the 80s
      </p>
      <p class="category-label">SCIENCE - NATURE</p>
    </section>

    <section class="front-cover">
      <h1 class="front-title">
        <span class="line-small">WHISPERS</span>
        <span class="line-huge">BENEATH</span>
        <span class="line-mid">THE AMBER</span>
        <span class="line-large">HORIZON</span>
      </h1>
    </section>
  </main>
</body>
</html>
```